Stationery Design Project

Would like to have the design elements we created in for our website (www.brook-estates.com), incorporated in a stationery design layout.
Updates
Colors used in the logo attachments do not need to be used. We are open to different color variations. Looking for a crisp, clean, modern update using the design elements in attachments and which can also be viewed on or website.
A note to designers:
Project Deadline Extended
Reason: Due to update in our project description and requirements, we have decided to extend the deadline of this project to provide ample opportunity to all designers participating .
Requirements
Must have
- Must have continuity with the theme and design features used in our website. Have attached .jpg images of some of the design elements.

```html
<!DOCTYPE html>
<html lang="en">
<head>
<meta charset="utf-8">
<title>Brook Estates Letterhead</title>
<link rel="stylesheet" href="https://fonts.googleapis.com/css2?family=PT+Sans:wght@400&display=swap">
<style>
  :root {
    --paper: #ffffff;
    --ink: #3a3a3a;
    --muted: #555555;
    --brand-blue: #1f7bbf;
    --brand-green: #5cb848;
    --wash-green: #e6f2e6;
    --rule: #c9c9c9;
  }
  html, body {
    margin: 0;
    padding: 0;
    width: 967px;
    height: 1200px;
    overflow: hidden;
    background: var(--paper);
  }
  .letterhead {
    position: relative;
    width: 967px;
    height: 1200px;
    background: var(--paper);
    font-family: "PT Sans", Arial, sans-serif;
    color: var(--ink);
  }
  .header-name {
    position: absolute;
    left: 78px;
    top: 80px;
    margin: 0;
    font-size: 46px;
    font-weight: 400;
    color: var(--ink);
    letter-spacing: 0.5px;
  }
  .contact-list {
    position: absolute;
    left: 738px;
    top: 86px;
    margin: 0;
    padding: 0 0 0 10px;
    list-style: none;
    border-left: 1px solid var(--rule);
    font-size: 15.5px;
    line-height: 21px;
    color: var(--muted);
  }
  .contact-list li {
    display: flex;
    align-items: center;
    gap: 4px;
  }
  .contact-list svg {
    width: 11px;
    height: 11px;
    flex: none;
  }
  .watermark {
    position: absolute;
    left: 400px;
    top: 465px;
    width: 300px;
    height: 300px;
    border-radius: 50%;
    background: var(--wash-green);
  }
  .footer-name {
    position: absolute;
    right: 52px;
    top: 1088px;
    margin: 0;
    font-size: 54px;
    font-weight: 400;
    line-height: 1;
    color: var(--brand-blue);
  }
  .footer-band {
    position: absolute;
    top: 1156px;
    height: 12px;
  }
  .footer-band--blue { left: 0; width: 476px; background: var(--brand-blue); }
  .footer-band--green { left: 486px; right: 0; background: var(--brand-green); }
  .address {
    position: absolute;
    left: 0;
    right: 0;
    top: 1175px;
    margin: 0;
    text-align: center;
    font-size: 15px;
    letter-spacing: 1px;
    color: var(--muted);
  }
</style>
</head>
<body>
<div class="letterhead">
  <p class="header-name">Brook</p>

  <ul class="contact-list">
    <li>
      <svg viewBox="0 0 12 12" aria-hidden="true"><path d="M3 1 L5 3.5 L4 5 Q5.5 7 7 8 L8.5 7 L11 9 L9.5 11 Q4 10 1 3 Z" fill="var(--brand-blue)"/></svg>
      (555) 214-3870
    </li>
    <li>
      <svg viewBox="0 0 12 12" aria-hidden="true"><rect x="3" y="1" width="6" height="4" fill="var(--brand-blue)"/><rect x="1" y="5" width="10" height="6" rx="1" fill="var(--brand-blue)"/></svg>
      (555) 214-3871
    </li>
    <li>
      <svg viewBox="0 0 12 12" aria-hidden="true"><rect x="1" y="3" width="10" height="6" fill="var(--brand-blue)"/></svg>
      info@brook-estates.com
    </li>
    <li>
      <svg viewBox="0 0 12 12" aria-hidden="true"><circle cx="6" cy="6" r="4.5" fill="var(--brand-blue)"/></svg>
      www.brook-estates.com
    </li>
  </ul>

  <div class="watermark" aria-hidden="true"></div>

  <p class="footer-name">Brook Estates</p>

  <div class="footer-band footer-band--blue"></div>
  <div class="footer-band footer-band--green"></div>

  <p class="address">212 Willow Bend Lane Suite 304, Dalton, GA 30720</p>
</div>
</body>
</html>
```